Building company requiring web site design

We need a web design for a new company based in Sydney called Marlow Building Co. We build and renovate new and existing homes for consumers. We would like to see design that use the colours red and grey. The final design should communicate innovative building but with old fashion quality, great customer service and attention to detail. I have already had a logo and stationary design completed and would like to use the these colour schemes
Updates

Target Market(s)

Home owners, investors

Industry/Entity Type

Building

Coding

Coded - Design and coding required

Number of Pages Required

5+ page

Requirements
Must have
• Home page, contact page, about us page, gallery page and testimonial page
Nice to have
• Contact form

```html
<!DOCTYPE html>
<html lang="en">
<head>
<meta charset="utf-8">
<title>Marlow Building Co.</title>
<link href="https://fonts.googleapis.com/css2?family=Bitter:wght@400;700&family=Lato:wght@400;700&display=swap" rel="stylesheet">
<style>
:root{
  --red:#b13f3f;
  --charcoal:#2f2f2f;
  --charcoal-2:#353535;
  --topbar:#2b2b2b;
  --ink:#222;
  --text:#333;
  --white:#fff;
}
*{margin:0;padding:0;box-sizing:border-box}
html,body{width:1200px;height:2410px;overflow:hidden;background:var(--white)}
body{font-family:'Lato',sans-serif;color:var(--text);position:relative}
.section{position:absolute;left:0;width:1200px}

/* top bar */
.topbar{top:0;height:43px;background:var(--topbar);color:#cfcfcf;font-size:14px}
.topbar .social{position:absolute;left:104px;top:12px;display:flex;gap:14px}
.topbar .social span{width:16px;height:16px;background:#bdbdbd;display:block}
.topbar .contact{position:absolute;right:100px;top:13px;display:flex;gap:40px;align-items:center}
.topbar .contact div{display:flex;gap:9px;align-items:center}

/* header */
.header{top:43px;height:111px;background:var(--white)}
.brand{position:absolute;left:100px;top:38px;display:flex;align-items:center;gap:10px;font-family:'Bitter',serif;font-weight:700;font-size:24px;color:var(--ink)}
.brand .mark{width:22px;height:22px;background:var(--red)}
.nav{position:absolute;right:100px;top:0;height:111px;display:flex}
.nav a{display:block;height:111px;line-height:111px;padding:0 26px;font-size:14px;color:var(--ink);text-decoration:none}
.nav a:last-child{padding-right:0}
.nav a.active{color:var(--red);border-bottom:3px solid var(--red);line-height:108px}

/* hero */
.hero{top:154px;height:429px;background:linear-gradient(100deg,#e3ddd2 0%,#d8cbb6 35%,#c9a56b 60%,#b98a45 80%,#e6e6e4 100%)}
.hero-box{position:absolute;left:100px;top:98px;width:397px;height:233px;background:rgba(45,45,45,.85);padding:18px 18px;color:var(--white)}
.hero-box h1{font-family:'Bitter',serif;font-weight:700;font-size:31px;line-height:38px}
.hero-box p{font-size:14.5px;line-height:22px;margin-top:14px;color:#eee}
.btn{display:inline-block;background:var(--red);color:var(--white);font-size:14px;font-weight:700;padding:0 16px;height:32px;line-height:32px;border-radius:3px}
.hero-box .btn{margin-top:14px}
.arrow{position:absolute;top:196px}

/* headings */
.title{text-align:center;font-family:'Bitter',serif;font-weight:400;font-size:31px;color:var(--ink)}
.title em{font-style:normal;color:var(--red)}
.title .rule{display:inline-block;width:78px;height:1px;background:var(--ink);vertical-align:middle;margin:0 16px}

/* about */
.about{top:583px;height:277px}
.about .title{margin-top:37px}
.about p{width:1000px;margin:22px auto 0;text-align:center;font-size:13.5px;line-height:27px;color:var(--ink)}
.about .btn-wrap{text-align:center;margin-top:20px}

/* services */
.services{top:860px;height:498px;background:var(--charcoal)}
.services .title{color:var(--white);margin-top:44px}
.services .title .rule{background:#aaa}
.cards{position:absolute;top:120px;left:100px;display:flex;gap:22px}
.card{width:233px;height:333px;background:var(--white);border-radius:3px;position:relative;overflow:hidden}
.card .top{height:119px;background:var(--red);color:var(--white);text-align:center;font-family:'Bitter',serif;font-size:22px;padding-top:16px}
.card .photo{position:absolute;left:52px;top:55px;width:128px;height:128px;border-radius:50%;border:3px solid var(--red);background:linear-gradient(135deg,#8d9aa3,#c9b58d)}
.card p{position:absolute;top:204px;left:12px;right:12px;text-align:center;font-size:13px;line-height:19px;color:var(--text)}
.card .btn{position:absolute;left:59px;top:277px;width:115px;padding:0;text-align:center}

/* gallery */
.gallery{top:1358px;height:498px}
.gallery .title{margin-top:37px}
.gallery .lead{text-align:center;font-size:13px;margin-top:20px;color:var(--ink)}
.tile{position:absolute}
.g-arrow{position:absolute;top:276px}

/* reviews */
.reviews{top:1856px;height:236px;background:linear-gradient(90deg,#2a2a2a,#3a3631,#2d2d2d)}
.reviews .title{color:var(--white);margin-top:36px}
.reviews .title .rule{background:#aaa}
.avatar{position:absolute;left:100px;top:82px;width:86px;height:86px;border-radius:50%;border:3px solid var(--white);background:linear-gradient(180deg,#c9c9c9,#6d7480)}
.reviewer{position:absolute;left:88px;top:178px;width:110px;text-align:center;color:var(--white);font-size:13px;font-weight:700}
.quote{position:absolute;left:207px;top:98px;width:860px;color:#f2f2f2;font-size:13px;line-height:24px}
.quote b{font-family:'Bitter',serif;font-size:22px;line-height:0}
.pager{position:absolute;left:1058px;top:172px;display:flex;gap:6px}

/* footer */
.footer{top:2092px;height:275px;background:var(--charcoal-2);color:#e4e4e4}
.fcol{position:absolute;top:43px}
.fcol h3{font-family:'Bitter',serif;font-weight:400;font-size:16px;color:var(--white);padding-bottom:6px;border-bottom:1px solid #666;display:inline-block}
.fcol ul{list-style:none;margin-top:10px}
.links li{font-size:13px;line-height:27px;padding-left:18px;position:relative}
.links li::before{content:"";position:absolute;left:0;top:11px;width:6px;height:6px;border:1px dotted #bbb}
.info li{font-size:13px;line-height:20px;padding-left:24px;position:relative;margin-top:14px}
.info svg{position:absolute;left:0;top:3px}
.follow li{font-size:13px;line-height:30px;display:flex;align-items:center;gap:12px}
.follow li span{width:20px;height:20px;background:#d6d6d6;display:block}
.footer-brand{position:absolute;left:852px;top:115px;display:flex;align-items:center;gap:10px;font-family:'Bitter',serif;font-weight:700;font-size:26px;color:#dcdcdc}
.footer-brand .mark{width:22px;height:22px;background:#dcdcdc}

/* bottom bar */
.bottombar{top:2367px;height:43px;background:var(--red);color:var(--white);font-size:13px;text-align:center;line-height:43px}
</style>
</head>
<body>

<div class="section topbar">
  <div class="social" aria-label="Social links"><span></span><span></span><span></span><span></span></div>
  <div class="contact">
    <div><svg width="14" height="14" viewBox="0 0 24 24"><path fill="#bbb" d="M6.6 10.8a15 15 0 006.6 6.6l2.2-2.2c.3-.3.7-.4 1-.2 1.1.4 2.3.6 3.6.6.6 0 1 .4 1 1V20c0 .6-.4 1-1 1A17 17 0 013 4c0-.6.4-1 1-1h3.5c.6 0 1 .4 1 1 0 1.3.2 2.5.6 3.6.1.3 0 .7-.2 1z"/></svg>0400-555-182</div>
    <div><svg width="15" height="12" viewBox="0 0 24 18"><path fill="#bbb" d="M0 0h24v18H0z"/><path fill="none" stroke="#2b2b2b" stroke-width="2" d="M1 1l11 9 11-9"/></svg>info@marlowbuildingco.com</div>
  </div>
</div>

<header class="section header">
  <div class="brand"><span class="mark"></span>Marlow Building Co.</div>
  <nav class="nav">
    <a class="active">HOME</a><a>ABOUT US</a><a>SERVICES</a><a>GALLERY</a><a>TESTIMONIALS</a><a>CONTACT</a>
  </nav>
</header>

<section class="section hero" role="img" aria-label="Photo of three smiling builders in hard hats and overalls holding plans and a drill">
  <div class="hero-box">
    <h1>Committed To Superior Quality and Results</h1>
    <p>Lorem ipsum dolor sit amet, consectetur adipiscing elit, sed do eiusmod tempor incididunt ut labore et dolore magna aliqua. Ut enim ad minim veniam</p>
    <span class="btn">Learn More</span>
  </div>
  <svg class="arrow" style="left:36px" width="20" height="36" viewBox="0 0 20 36"><path d="M18 2L2 18l16 16" fill="none" stroke="#fff" stroke-width="2"/></svg>
  <svg class="arrow" style="right:36px" width="20" height="36" viewBox="0 0 20 36"><path d="M2 2l16 16L2 34" fill="none" stroke="#fff" stroke-width="2"/></svg>
</section>

<section class="section about">
  <h2 class="title"><span class="rule"></span>About <em>Marlow Building Co.</em><span class="rule"></span></h2>
  <p>Lorem ipsum dolor sit amet, consectetur adipiscing elit, sed do eiusmod tempor incididunt ut labore et dolore magna aliqua. Ut enim ad minim veniam, quis nostrud exercitation ullamco laboris nisi ut aliquip ex ea commodo consequat. Duis aute irure dolor in reprehenderit in voluptate velit esse cillum dolore eu fugiat nulla pariatur. Excepteur sint occaecat cupidatat non proident, sunt in culpa qui officia deserunt mollit anim id est laborum.</p>
  <div class="btn-wrap"><span class="btn">Read More</span></div>
</section>

<section class="section services">
  <h2 class="title"><span class="rule"></span>Our Services<span class="rule"></span></h2>
  <div class="cards">
    <div class="card"><div class="top">Building</div><div class="photo" role="img" aria-label="Photo of two builders in hard hats reviewing work"></div><p>Sed ut perspiciatis unde omnis iste natus error sit voluptatem and an accusantium doloremque.</p><span class="btn">Read More</span></div>
    <div class="card"><div class="top">House Renovation</div><div class="photo" role="img" aria-label="Photo of a builder working on timber framing"></div><p>Sed ut perspiciatis unde omnis iste natus error sit voluptatem and an accusantium doloremque.</p><span class="btn">Read More</span></div>
    <div class="card"><div class="top">Electricity</div><div class="photo" role="img" aria-label="Photo of an electrician testing a switchboard"></div><p>Sed ut perspiciatis unde omnis iste natus error sit voluptatem and an accusantium doloremque.</p><span class="btn">Read More</span></div>
    <div class="card"><div class="top">Flooring</div><div class="photo" role="img" aria-label="Photo of a worker laying floor boards"></div><p>Sed ut perspiciatis unde omnis iste natus error sit voluptatem and an accusantium doloremque.</p><span class="btn">Read More</span></div>
  </div>
</section>

<section class="section gallery">
  <h2 class="title"><span class="rule"></span>Our <em>Gallery</em><span class="rule"></span></h2>
  <p class="lead">Sed ut perspiciatis unde omnis iste natus error sit voluptatem accusantium doloremque laudantium, totam rem aperiam, eaque ipsa quae ab illo</p>
  <div class="tile" style="left:100px;top:160px;width:295px;height:295px;background:linear-gradient(135deg,#3c3a33,#252525);box-shadow:0 8px 10px rgba(0,0,0,.25)" role="img" aria-label="Photo of builders in hard hats reading plans">
    <svg style="position:absolute;left:133px;top:133px" width="28" height="28" viewBox="0 0 28 28"><circle cx="14" cy="14" r="14" fill="#b13f3f"/><circle cx="13" cy="13" r="5" fill="none" stroke="#fff" stroke-width="2"/><path d="M17 17l4 4" stroke="#fff" stroke-width="2"/></svg>
  </div>
  <div class="tile" style="left:411px;top:160px;width:189px;height:147px;background:linear-gradient(160deg,#d9cbb7,#a2672f)" role="img" aria-label="Photo of a worker laying a timber floor"></div>
  <div class="tile" style="left:411px;top:321px;width:189px;height:134px;background:linear-gradient(135deg,#9fd8c0,#e8e8e8)" role="img" aria-label="Photo of a painter rolling a wall mint green"></div>
  <div class="tile" style="left:614px;top:160px;width:278px;height:122px;background:linear-gradient(135deg,#8b6a4c,#d7d0c4)" role="img" aria-label="Photo of a worker fitting a ceiling panel"></div>
  <div class="tile" style="left:614px;top:297px;width:278px;height:158px;background:linear-gradient(180deg,#a9bfdc,#c7a57a)" role="img" aria-label="Photo of a builder in front of a new brick home"></div>
  <div class="tile" style="left:905px;top:160px;width:197px;height:295px;background:linear-gradient(180deg,#e9e3d8,#c6a67c)" role="img" aria-label="Photo of an attic under construction with timber framing"></div>
  <svg class="g-arrow" style="left:50px" width="18" height="34" viewBox="0 0 18 34"><path d="M16 2L2 17l14 15" fill="none" stroke="#444" stroke-width="2"/></svg>
  <svg class="g-arrow" style="right:50px" width="18" height="34" viewBox="0 0 18 34"><path d="M2 2l14 15L2 32" fill="none" stroke="#444" stroke-width="2"/></svg>
</section>

<section class="section reviews">
  <h2 class="title"><span class="rule"></span>Customer Reviews<span class="rule"></span></h2>
  <div class="avatar" role="img" aria-label="Portrait photo of the reviewer"></div>
  <div class="reviewer">Tempor Mech</div>
  <p class="quote"><b>“</b>Libris ponderum eloquentiam his, vix te nominati porte. At vel tor quatos accommodare, falli tamur volumus cumte, accusata voluptatum and an inusu. Dolorum appetere nominati melcu possesca evolali bera vissen amei. Porro fabellas explicari nam, eirmod minimum omnes quevixcu, suas sed disputationi an mei. Tempor doming mentitum ex pro, pri augue aliqua eos nepercipit suscipiantur, odio alienum per petua eum no.<b>”</b></p>
  <div class="pager">
    <svg width="16" height="16" viewBox="0 0 16 16"><circle cx="8" cy="8" r="7" fill="none" stroke="#fff"/><path d="M9.5 4.5L6 8l3.5 3.5" fill="none" stroke="#fff"/></svg>
    <svg width="16" height="16" viewBox="0 0 16 16"><circle cx="8" cy="8" r="7" fill="none" stroke="#fff"/><path d="M6.5 4.5L10 8l-3.5 3.5" fill="none" stroke="#fff"/></svg>
  </div>
</section>

<footer class="section footer">
  <div class="fcol" style="left:100px">
    <h3>Quick Links</h3>
    <ul class="links"><li>Home</li><li>About Us</li><li>Services</li><li>Gallery</li><li>Testimonials</li><li>Contact Us</li></ul>
  </div>
  <div class="fcol" style="left:336px">
    <h3>Contact Information</h3>
    <ul class="info">
      <li><svg width="12" height="16" viewBox="0 0 12 16"><path fill="#fff" d="M6 0a6 6 0 016 6c0 4-6 10-6 10S0 10 0 6a6 6 0 016-6zm0 3.5a2.5 2.5 0 100 5 2.5 2.5 0 000-5z"/></svg>100 Kent Lane St, Lorem ipsum<br>dolor sit amet, VIC 3226</li>
      <li style="margin-top:18px"><svg width="13" height="13" viewBox="0 0 24 24"><path fill="#fff" d="M6.6 10.8a15 15 0 006.6 6.6l2.2-2.2c.3-.3.7-.4 1-.2 1.1.4 2.3.6 3.6.6.6 0 1 .4 1 1V20c0 .6-.4 1-1 1A17 17 0 013 4c0-.6.4-1 1-1h3.5c.6 0 1 .4 1 1 0 1.3.2 2.5.6 3.6.1.3 0 .7-.2 1z"/></svg>+0400-555-182</li>
      <li style="margin-top:26px"><svg width="14" height="11" viewBox="0 0 24 18"><path fill="#fff" d="M0 0h24v18H0z"/><path fill="none" stroke="#353535" stroke-width="2" d="M1 1l11 9 11-9"/></svg>info@marlowbuildingco.com</li>
    </ul>
  </div>
  <div class="fcol" style="left:632px">
    <h3>Follow Us</h3>
    <ul class="follow"><li><span></span>Socialbook</li><li><span></span>Chirper</li><li><span></span>Circles+</li><li><span></span>Worklink</li></ul>
  </div>
  <div class="footer-brand"><span class="mark"></span>Marlow Building Co.</div>
</footer>

<div class="section bottombar">© 2016 Marlow Building Co. | All Rights Reserved.</div>

</body>
</html>
```